professional business card

A Clean looking business card for a money transfer company. Our company is call Velorix= Transfer + Send = Transcend (next level)
to show professionalism as well as some effects to show digital tech.

1 side to have position, name and address
2 side to have company name and show that we provide money exchange and cross-border money transfer

Target Market(s)

Remittance companies and high net worth individuals

Industry/Entity Type

Finance

Contact Information for Business Card

Name, address, email, title, services- money exchange and cross-border remittance

Requirements
Nice to have
• Digital age feel

```html
<!DOCTYPE html>
<html lang="en">
<head>
<meta charset="utf-8">
<title>Velorix Business Card</title>
<link href="https://fonts.googleapis.com/css2?family=Montserrat:wght@400;500;600;700&display=swap" rel="stylesheet">
<style>
  :root {
    --slate: #36434d;
    --slate-deep: #2d3740;
    --slate-soft: #46555f;
    --teal: #72d0dd;
    --paper: #fbfbfa;
    --ink: #3a4650;
    --muted: #5a666f;
    --rule: #b9bec2;
    --backdrop: #e6e8ea;
  }
  * { box-sizing: border-box; margin: 0; padding: 0; }
  html, body {
    width: 1200px; height: 901px; overflow: hidden;
    background: var(--backdrop);
    font-family: "Montserrat", sans-serif;
  }
  .sheet {
    position: relative; width: 1200px; height: 901px;
    display: flex; flex-direction: column; align-items: center; justify-content: center; gap: 40px;
  }
  .card {
    position: relative; width: 660px; height: 377px; overflow: hidden;
    box-shadow: 0 12px 30px rgba(30, 40, 50, 0.18);
  }

  /* Shared brand lockup */
  .brand { position: absolute; display: flex; align-items: center; gap: 12px; white-space: nowrap; }
  .brand-dot { width: 30px; height: 30px; border-radius: 50%; background: var(--teal); flex: none; }
  .brand-name { font-weight: 600; letter-spacing: 3px; text-transform: uppercase; line-height: 1; }

  /* Front */
  .card-front { background: var(--paper); color: var(--ink); }
  .card-front .brand { left: 48px; top: 62px; }
  .card-front .brand-name { font-size: 34px; color: var(--slate); }
  .rule-main { position: absolute; left: 48px; top: 138px; width: 348px; height: 1px; background: var(--rule); }
  .holder { position: absolute; left: 410px; top: 122px; white-space: nowrap; }
  .holder-name { font-size: 23px; font-weight: 600; letter-spacing: 1.5px; text-transform: uppercase; color: var(--slate); line-height: 1.1; }
  .holder-title { font-size: 15px; font-weight: 500; letter-spacing: 0.6px; color: var(--muted); margin-top: 3px; }
  .rule-short { position: absolute; left: 612px; top: 134px; width: 28px; height: 1px; background: var(--rule); }
  .contacts { position: absolute; left: 48px; top: 172px; list-style: none; display: flex; flex-direction: column; gap: 12px; }
  .contact { display: flex; align-items: flex-start; gap: 16px; font-size: 15px; letter-spacing: 0.5px; line-height: 1.3; color: var(--ink); }
  .contact svg { width: 16px; height: 16px; flex: none; margin-top: 1px; fill: var(--teal); }
  .band-teal { position: absolute; left: 0; bottom: 0; width: 100%; height: 12px; background: var(--teal); }
  .band-slate {
    position: absolute; right: 0; bottom: 0; width: 150px; height: 26px; background: var(--slate);
    clip-path: polygon(8px 0, 100% 0, 100% 100%, 0 100%);
  }

  /* Back */
  .card-back { background: var(--slate); }
  .world-map {
    position: absolute; inset: 24px 30px;
    background: radial-gradient(ellipse at 50% 50%, var(--slate-soft) 0%, var(--slate) 72%);
    border-radius: 40px;
  }
  .back-lockup {
    position: absolute; left: 50%; top: 50%; transform: translate(-50%, -50%);
    display: flex; flex-direction: column; align-items: center; gap: 18px;
  }
  .card-back .brand { position: static; }
  .card-back .brand-name { font-size: 44px; color: #ffffff; }
  .card-back .brand-dot { width: 38px; height: 38px; }
  .services {
    display: flex; align-items: center; gap: 12px;
    font-size: 13px; font-weight: 500; letter-spacing: 2px; text-transform: uppercase; color: #d5dde2;
    white-space: nowrap;
  }
  .services-sep { width: 5px; height: 5px; border-radius: 50%; background: var(--teal); }
  .signal-line { position: absolute; left: 0; bottom: 0; width: 100%; height: 4px; background: linear-gradient(90deg, transparent, var(--teal), transparent); opacity: 0.7; }
</style>
</head>
<body>
<main class="sheet">
  <section class="card card-front" aria-label="Card front">
    <div class="brand"><span class="brand-dot"></span><span class="brand-name">Velorix</span></div>
    <div class="rule-main"></div>
    <div class="holder">
      <p class="holder-name">Marcus Hale</p>
      <p class="holder-title">Managing Director</p>
    </div>
    <div class="rule-short"></div>
    <ul class="contacts">
      <li class="contact">
        <svg viewBox="0 0 24 24" aria-hidden="true"><path d="M6.6 10.8a15.1 15.1 0 0 0 6.6 6.6l2.2-2.2a1 1 0 0 1 1-.25 11.4 11.4 0 0 0 3.6.6 1 1 0 0 1 1 1V20a1 1 0 0 1-1 1A17 17 0 0 1 3 4a1 1 0 0 1 1-1h3.5a1 1 0 0 1 1 1c0 1.25.2 2.45.6 3.6a1 1 0 0 1-.25 1z"/></svg>
        <span>00998877661</span>
      </li>
      <li class="contact">
        <svg viewBox="0 0 24 24" aria-hidden="true"><path d="M2 5h20v14H2z M4 7v.4l8 5.2 8-5.2V7z" fill-rule="evenodd"/></svg>
        <span>marcus@velorix.com</span>
      </li>
      <li class="contact">
        <svg viewBox="0 0 24 24" aria-hidden="true"><path d="M12 2a7 7 0 0 0-7 7c0 5.2 7 13 7 13s7-7.8 7-13a7 7 0 0 0-7-7zm0 9.5A2.5 2.5 0 1 1 12 6.5a2.5 2.5 0 0 1 0 5z"/></svg>
        <span>Lorem ipsum dolor sit amet,<br>consectetur.</span>
      </li>
    </ul>
    <div class="band-teal"></div>
    <div class="band-slate"></div>
  </section>

  <section class="card card-back" aria-label="Card back">
    <div class="world-map" role="img" aria-label="Faint world map showing cross-border reach"></div>
    <div class="back-lockup">
      <div class="brand"><span class="brand-dot"></span><span class="brand-name">Velorix</span></div>
      <p class="services"><span>Money Exchange</span><span class="services-sep"></span><span>Cross-Border Remittance</span></p>
    </div>
    <div class="signal-line"></div>
  </section>
</main>
</body>
</html>
```